KTR Motorhaus Automotive Repair and Service Shop

I need an informative and interactive website for my automotive service and repair shop. The website must give information about the shop, as well as the ability to make bookings and a forums page for our users to use and set up an account with us, in which we can give promotions via email. We are located in Pompano Beach Florida and our company name is KTR Motorhaus. Our color scheme is a red for accent and grey (neutral color) as a base. The design must communicate our message and be able to grow should we decide to retail parts in the future. One of the websites I take the highest inspiration from is http://www.lanvexbodyshop.example/. Although I do not have as nearly as many certifications as them. Attached are some images of our shop so you can see how clean and modern our building is, and I would like our website to match our feel. Thank you.

Target Market(s)

Automotive Enthusiasts

Industry/Entity Type

Automotive

Contact Information for Business Card

KTR Motorhaus /954 718 6402 /rohan@ktrmotorhaus.example/ 512 NE 9th St Pompano Beach FL 33062/ any other info needed please ask me

Coding

Coded - Design and coding required

Number of Pages Required

5+ page

Font styles to use
Sans Serif

Requirements
Must have
• Name, logo, contact info, location, phone number
Nice to have
• Building is very modern, would like a business card to match
Should not have
• Not to playful or vibrant

```html
<!DOCTYPE html>
<html lang="en">
<head>
<meta charset="utf-8">
<title>KTR Motorhaus</title>
<link rel="stylesheet" href="https://fonts.googleapis.com/css2?family=Russo+One&family=Lato:wght@400;700&family=Merriweather:wght@300;400;700&display=swap">
<style>
:root{
  --red:#e0080f;
  --topbar:#0f3a34;
  --ink:#111;
  --text:#333;
  --muted:#555;
  --grey:#ebebeb;
  --soft:#f4f4f4;
  --footer:#1f1f1f;
  --white:#fff;
}
*{box-sizing:border-box;margin:0;padding:0}
html,body{width:1200px;height:3757px;overflow:hidden}
body{position:relative;background:var(--white);font-family:'Merriweather',serif;color:var(--text)}
.abs{position:absolute}
.heading{font-family:'Russo One',sans-serif;color:var(--ink);text-align:center;width:1200px;left:0;font-size:42px;letter-spacing:1px}
.btn{position:absolute;display:flex;align-items:center;justify-content:center;gap:8px;border-radius:28px;font-family:'Lato',sans-serif;font-weight:700;font-size:18px;background:var(--red);color:var(--white);border:3px solid var(--red)}
.btn.outline{background:var(--white);color:var(--red)}
.btn svg{width:16px;height:16px}
.photo{position:absolute}
/* top bar */
.topbar{left:0;top:0;width:1200px;height:40px;background:var(--topbar);color:var(--white);font-family:'Merriweather',serif;font-size:15px}
.topbar .social{left:86px;top:12px;display:flex;gap:22px}
.topbar .social span{width:14px;height:14px;border-radius:50%;background:rgba(255,255,255,.85);display:block}
.topbar .mail{left:650px;top:10px;display:flex;gap:12px;align-items:center}
.topbar .divider{left:916px;top:0;width:1px;height:40px;background:rgba(255,255,255,.25)}
.topbar .phone{left:953px;top:8px;display:flex;gap:12px;align-items:center;font-size:19px}
/* header */
.header{left:0;top:40px;width:1200px;height:81px;background:var(--white)}
.logo{left:90px;top:22px;display:flex;align-items:center;gap:10px;font-family:'Lato',sans-serif;font-weight:700;font-size:26px;color:var(--ink)}
.logo i{width:18px;height:18px;background:var(--red);display:block}
.nav{left:370px;top:30px;display:flex;gap:38px;font-size:16px;color:#333}
.nav .active{color:var(--red);font-weight:700}
.login{left:952px;top:58px;width:158px;height:53px}
/* hero */
.hero{left:0;top:121px;width:1200px;height:576px;background:linear-gradient(135deg,#3b3f44 0%,#2a2c30 45%,#51545a 70%,#222 100%)}
.hero::after{content:"";position:absolute;inset:0;background:rgba(0,0,0,.35)}
.hero-content{left:0;top:168px;width:1200px;text-align:center;color:var(--white);z-index:2}
.hero-title{font-family:'Russo One',sans-serif;font-size:58px;letter-spacing:1px}
.hero-sub{font-size:22px;line-height:32px;font-weight:300;margin-top:18px}
.hero-arrow{z-index:2;top:378px}
/* services */
.service{top:879px;width:242px;height:299px}
.service span{position:absolute;left:16px;bottom:16px;font-family:'Merriweather',serif;font-weight:700;font-size:21px;line-height:29px;color:var(--white);z-index:2}
/* welcome */
.welcome-text{left:136px;top:1348px;width:928px;font-size:16px;line-height:30.5px;text-align:justify;text-align-last:center;color:#333}
/* about */
.about-bg{left:0;top:1750px;width:768px;height:437px;background:var(--grey)}
.about-title{left:90px;top:1790px;font-family:'Russo One',sans-serif;font-size:40px;color:var(--ink)}
.about-text{left:90px;top:1848px;width:478px;font-size:15px;line-height:36px;color:#333}
/* blog */
.post{top:2359px;width:323px;height:481px;border-left:7px solid var(--red);border-bottom:7px solid var(--red);background:var(--white);box-shadow:0 0 8px rgba(0,0,0,.06)}
.post .img{position:absolute;left:0;top:0;width:316px;height:248px}
.post .avatar{position:absolute;left:220px;top:205px;width:87px;height:87px;border-radius:50%;border:4px solid var(--white);z-index:2}
.post h3{position:absolute;left:20px;top:282px;width:240px;font-weight:300;font-size:23px;line-height:28px;color:#222}
.post p{position:absolute;left:20px;top:354px;width:280px;font-size:14.5px;line-height:28px;color:#666;font-weight:300}
.post .more{position:absolute;right:10px;top:446px;font-size:14px;font-weight:700;color:var(--red)}
.post .tag{position:absolute;left:50px;top:154px;width:214px;height:94px;background:var(--red);color:var(--white);font-size:14px;line-height:28px;text-align:center;padding-top:20px;font-weight:300;z-index:1}
/* testimonials */
.testi-bg{left:0;top:2960px;width:1200px;height:456px;background:var(--soft)}
.testi-photo{left:125px;top:3103px;width:209px;height:209px;border-radius:50%}
.quote{left:373px;top:3132px;width:710px;font-size:15.5px;line-height:32px;color:#555;font-weight:300}
.testi-name{left:373px;top:3240px;font-size:15px;font-weight:700;color:#222}
.testi-loc{left:373px;top:3265px;font-family:'Lato',sans-serif;font-style:italic;font-size:12px;color:#888}
/* footer */
.footer{left:0;top:3416px;width:1200px;height:341px;background:var(--footer);color:var(--white)}
.footer .logo{color:var(--white);left:120px;top:64px}
.fsocial{top:168px;width:42px;height:42px;border-radius:50%;border:1px solid #444;background:#2a2a2a}
.fsocial i{position:absolute;left:16px;top:16px;width:9px;height:9px;border-radius:50%;background:#ddd}
.copy{left:90px;top:262px;font-size:12.5px;line-height:23px;color:#ddd}
.fhead{top:66px;font-size:21px;font-weight:300}
.flist{top:116px;font-size:14px;line-height:30.2px;font-weight:300;color:#eee;list-style:none}
.news{left:809px;top:126px;width:301px;height:40px;border-radius:20px;background:#2b2b2b;font-family:'Lato',sans-serif;font-size:13px;color:#ddd;padding:12px 22px}
.news svg{position:absolute;right:22px;top:12px}
.query{left:809px;top:206px;font-size:21px;font-weight:300}
.qphone{left:809px;top:240px;display:flex;gap:10px;align-items:center;font-family:'Lato',sans-serif;font-size:19px}
</style>
</head>
<body>

<div class="abs topbar">
  <div class="abs social"><span></span><span></span><span></span><span></span><span></span></div>
  <div class="abs mail">
    <svg width="18" height="14" viewBox="0 0 18 14"><rect x="1" y="1" width="16" height="12" rx="1" fill="none" stroke="#fff" stroke-width="1.6"/><path d="M1 2l8 6 8-6" fill="none" stroke="#fff" stroke-width="1.6"/></svg>
    rohan@ktrmotorhaus.example
  </div>
  <div class="abs divider"></div>
  <div class="abs phone">
    <svg width="16" height="16" viewBox="0 0 24 24"><path d="M6.6 10.8a15 15 0 0 0 6.6 6.6l2.2-2.2a1 1 0 0 1 1-.25 11.4 11.4 0 0 0 3.6.57 1 1 0 0 1 1 1V20a1 1 0 0 1-1 1A17 17 0 0 1 3 4a1 1 0 0 1 1-1h3.5a1 1 0 0 1 1 1c0 1.25.2 2.45.57 3.6a1 1 0 0 1-.25 1z" fill="#fff"/></svg>
    954 718 6402
  </div>
</div>

<header class="abs header">
  <div class="abs logo"><i></i>KTR MOTORHAUS</div>
  <nav class="abs nav"><span class="active">Home</span><span>About Us</span><span>Services</span><span>Forum</span><span>Blog</span><span>Contact Us</span></nav>
</header>
<div class="btn login">Login <svg viewBox="0 0 16 16"><circle cx="8" cy="8" r="7" fill="none" stroke="#fff" stroke-width="1.6"/><path d="M5 8h6M8.5 5.5 11 8l-2.5 2.5" fill="none" stroke="#fff" stroke-width="1.6"/></svg></div>

<section class="abs hero" role="img" aria-label="Mechanic smiling beside a car wheel in a workshop"></section>
<div class="abs hero-content">
  <div class="hero-title">KTR MOTORHAUS</div>
  <div class="hero-sub">Lorem ipsum dolor sit amet, consectetur adipiscing elit, sed do eiusmod<br>tempor incididunt ut labore et dolore magna aliqua.</div>
</div>
<svg class="abs hero-arrow" style="left:90px" width="16" height="24" viewBox="0 0 16 24"><path d="M12 3 4 12l8 9" fill="none" stroke="#fff" stroke-width="3"/></svg>
<svg class="abs hero-arrow" style="left:1094px" width="16" height="24" viewBox="0 0 16 24"><path d="M4 3l8 9-8 9" fill="none" stroke="#fff" stroke-width="3"/></svg>
<div class="btn" style="left:500px;top:481px;width:201px;height:54px;z-index:2">Read More <svg viewBox="0 0 16 16"><circle cx="8" cy="8" r="7" fill="none" stroke="#fff" stroke-width="1.6"/><path d="M5 8h6M8.5 5.5 11 8l-2.5 2.5" fill="none" stroke="#fff" stroke-width="1.6"/></svg></div>

<h2 class="abs heading" style="top:810px">SERVICES</h2>
<div class="abs service" style="left:90px"><div class="photo" style="inset:0;background:linear-gradient(160deg,#5a6b80,#2c3846)" role="img" aria-label="Mechanic holding a wrench in a garage"></div><span>Auto Repair and<br>Service</span></div>
<div class="abs service" style="left:349px"><div class="photo" style="inset:0;background:linear-gradient(160deg,#6b6660,#2b2826)" role="img" aria-label="Technician working on a lifted wheel"></div><span>Full Diagnostics<br>and Repairs</span></div>
<div class="abs service" style="left:608px"><div class="photo" style="inset:0;background:linear-gradient(160deg,#8a8c90,#1d1e22)" role="img" aria-label="Polishing the headlight of a black car"></div><span>Custom Work</span></div>
<div class="abs service" style="left:868px"><div class="photo" style="inset:0;background:linear-gradient(160deg,#b3b6ba,#3d3f44)" role="img" aria-label="Engine bay with jumper cables attached"></div><span>Engine Repair</span></div>

<h2 class="abs heading" style="top:1277px">WELCOME TO KTRMOTORHAUS</h2>
<p class="abs welcome-text">Lorem ipsum dolor sit amet, consectetur adipiscing elit, sed do eiusmod tempor incididunt ut labore et dolore magna aliqua. Ut enim ad minim veniam, quis nostrud exercitation ullamco laboris nisi ut aliquip ex ea commodo consequat. Duis aute irure dolor in reprehenderit in voluptate velit esse cillum dolore eu fugiat nulla pariatur. Excepteur sint occaecat cupidatat non proident, sunt in culpa qui officia deserunt mollit anim id est laborum.</p>
<div class="btn" style="left:388px;top:1512px;width:202px;height:52px">Read More <svg viewBox="0 0 16 16"><circle cx="8" cy="8" r="7" fill="none" stroke="#fff" stroke-width="1.6"/><path d="M5 8h6M8.5 5.5 11 8l-2.5 2.5" fill="none" stroke="#fff" stroke-width="1.6"/></svg></div>
<div class="btn outline" style="left:609px;top:1512px;width:202px;height:52px">Book Now <svg viewBox="0 0 16 16"><circle cx="8" cy="8" r="7" fill="none" stroke="#e0080f" stroke-width="1.6"/><path d="M5 8h6M8.5 5.5 11 8l-2.5 2.5" fill="none" stroke="#e0080f" stroke-width="1.6"/></svg></div>

<div class="abs about-bg"></div>
<h2 class="abs about-title">ABOUT US</h2>
<p class="abs about-text">Sed ut perspiciatis unde omnis iste natus error sit voluptatem ium doloremque laudantium, totam rem aperiam, eaque ipsa quae ab illo inventore veritatis et quasi architecto beatae vitae dicta sunt cabo. Nemo enim ipsam voluptatem quia voluptas sit aspernatur aut odit aut fugit, sed quia consequuntur magni dolores eos qui rationelutem sequi nesciunt.</p>
<div class="btn" style="left:90px;top:2080px;width:202px;height:53px">Read More <svg viewBox="0 0 16 16"><circle cx="8" cy="8" r="7" fill="none" stroke="#fff" stroke-width="1.6"/><path d="M5 8h6M8.5 5.5 11 8l-2.5 2.5" fill="none" stroke="#fff" stroke-width="1.6"/></svg></div>
<div class="photo" style="left:595px;top:1688px;width:605px;height:438px;background:linear-gradient(120deg,#4a5a78,#8894a8 55%,#c23a3a 80%,#5a6070)" role="img" aria-label="Smiling mechanic in a red shirt under a lifted car"></div>

<h2 class="abs heading" style="top:2283px">LATEST BLOG</h2>
<article class="abs post" style="left:90px">
  <div class="img" style="background:linear-gradient(150deg,#c9cdd2,#7b7f86)" role="img" aria-label="Mechanic inspecting an engine under an open hood"></div>
  <div class="avatar" style="background:#b9876c" role="img" aria-label="Author portrait"></div>
  <h3>Lorem ipsum dolor sit amet</h3>
  <p>Lorem ipsum dolor sit met,onsectetur adipiscing elit, sed do eiusmod empor incididunt ut labore et dolore</p>
  <span class="more">Read More</span>
</article>
<article class="abs post" style="left:438px">
  <div class="img" style="background:linear-gradient(150deg,#4b5566,#1f2530)" role="img" aria-label="Mechanic in a cap working on an engine"></div>
  <div class="tag">KTR Motorhaus / By Admin<br>Jan25,2020</div>
  <div class="avatar" style="background:#8a7a70" role="img" aria-label="Author portrait"></div>
  <h3>Lorem ipsum dolor sit amet</h3>
  <p>Lorem ipsum dolor sit met,onsectetur adipiscing elit, sed do eiusmod empor incididunt ut labore et dolore</p>
  <span class="more">Read More</span>
</article>
<article class="abs post" style="left:786px">
  <div class="img" style="background:linear-gradient(150deg,#d6dade,#555b63)" role="img" aria-label="Technician fitting a car windshield"></div>
  <div class="avatar" style="background:#c49a7c" role="img" aria-label="Author portrait"></div>
  <h3>Lorem ipsum dolor sit amet</h3>
  <p>Lorem ipsum dolor sit met,onsectetur adipiscing elit, sed do eiusmod empor incididunt ut labore et dolore</p>
  <span class="more">Read More</span>
</article>

<div class="abs testi-bg"></div>
<h2 class="abs heading" style="top:3041px">TESTIMONIALS</h2>
<svg class="abs" style="left:38px;top:3196px" width="14" height="26" viewBox="0 0 14 26"><path d="M12 2 2 13l10 11" fill="none" stroke="#888" stroke-width="1.5"/></svg>
<svg class="abs" style="left:1150px;top:3196px" width="14" height="26" viewBox="0 0 14 26"><path d="M2 2l10 11-10 11" fill="none" stroke="#888" stroke-width="1.5"/></svg>
<div class="abs testi-photo" style="background:radial-gradient(circle at 50% 40%,#c9a88e,#6b5446 70%,#ddd 71%)" role="img" aria-label="Customer portrait"></div>
<svg class="abs" style="left:336px;top:3136px" width="28" height="18" viewBox="0 0 28 18"><circle cx="7" cy="11" r="6" fill="#e0080f"/><path d="M1 11C1 5 5 1 10 1" stroke="#e0080f" stroke-width="3" fill="none"/><circle cx="21" cy="11" r="6" fill="#e0080f"/><path d="M15 11C15 5 19 1 24 1" stroke="#e0080f" stroke-width="3" fill="none"/></svg>
<p class="abs quote">&nbsp;&nbsp;&nbsp;&nbsp;&nbsp;&nbsp;Lorem ipsum dolor sit amet, consectetur adipiscing elit, sed do eiusmod tempor incididunt ut labore et dolore magna aliqua. Ut enim ad minim veniam, quis nostrud exercitation ullamco laboris nisi ut aliquip ex ea commodo consequat.</p>
<svg class="abs" style="left:682px;top:3208px" width="28" height="18" viewBox="0 0 28 18"><circle cx="7" cy="7" r="6" fill="#e0080f"/><path d="M13 7c0 6-4 10-9 10" stroke="#e0080f" stroke-width="3" fill="none"/><circle cx="21" cy="7" r="6" fill="#e0080f"/><path d="M27 7c0 6-4 10-9 10" stroke="#e0080f" stroke-width="3" fill="none"/></svg>
<div class="abs testi-name">Mara Wells</div>
<div class="abs testi-loc">USA</div>

<footer class="abs footer">
  <div class="abs logo"><i></i>KTR MOTORHAUS</div>
  <div class="abs fsocial" style="left:88px"><i></i></div>
  <div class="abs fsocial" style="left:141px"><i></i></div>
  <div class="abs fsocial" style="left:196px"><i></i></div>
  <div class="abs fsocial" style="left:249px"><i></i></div>
  <p class="abs copy">Copyright © 2020 The Company Name.<br>All rights reserved.</p>
  <div class="abs fhead" style="left:395px">Links</div>
  <ul class="abs flist" style="left:395px"><li>Home</li><li>About Us</li><li>Services</li><li>Forum</li><li>Blog</li><li>Contact Us</li></ul>
  <div class="abs fhead" style="left:542px">Contact Us</div>
  <ul class="abs flist" style="left:542px;width:200px"><li>KTR Motorhaus</li><li>rohan@ktrmotorhaus.example</li><li>512 NE 9th St Pompano</li><li>Beach FL 33062</li></ul>
  <div class="abs fhead" style="left:809px">Newsletter</div>
  <div class="abs news">Enter Your Email Address
    <svg width="16" height="16" viewBox="0 0 16 16"><path d="M15 1 1 7l5 2 2 5z" fill="#fff"/></svg>
  </div>
  <div class="abs query">Any Query</div>
  <div class="abs qphone"><svg width="15" height="15" viewBox="0 0 24 24"><path d="M6.6 10.8a15 15 0 0 0 6.6 6.6l2.2-2.2a1 1 0 0 1 1-.25 11.4 11.4 0 0 0 3.6.57 1 1 0 0 1 1 1V20a1 1 0 0 1-1 1A17 17 0 0 1 3 4a1 1 0 0 1 1-1h3.5a1 1 0 0 1 1 1c0 1.25.2 2.45.57 3.6a1 1 0 0 1-.25 1z" fill="#fff"/></svg>954 718 6402</div>
</footer>

</body>
</html>
```